Property Auctions with Gareth Pemberley

Podcast cover art 3000px by 3000px. Eye catching for a weekly podcast. The words should read Property Auctions (large font) with Gareth Pemberley (smaller font)

I would like the font and colours to be similar to my book, a copy of which I have attached.

New and experienced property investors looking to purchase at a property auction

```html
<!DOCTYPE html>
<html lang="en">
<head>
<meta charset="utf-8">
<title>Property Auctions with Gareth Pemberley – Podcast Cover</title>
<link href="https://fonts.googleapis.com/css2?family=Archivo+Black&family=Raleway:wght@200&display=swap" rel="stylesheet">
<style>
  :root {
    --wall-light: #5b6264;
    --wall-mid: #41474a;
    --wall-dark: #2a2e30;
    --silver: #e8eef2;
    --silver-edge: #8fa1ad;
    --gold-top: #e2a81e;
    --gold-bottom: #c4840f;
    --red-top: #d0361b;
    --red-bottom: #a5200f;
    --name-fill: #2b2e30;
    --name-edge: #b4bbbe;
    --photo-top: #8a7f78;
    --photo-mid: #c9c6c4;
    --photo-suit: #34363e;
    --photo-bottom: #1c1e24;
  }
  html, body {
    margin: 0;
    padding: 0;
    overflow: hidden;
    background: var(--wall-dark);
  }
  .cover {
    position: relative;
    width: 1200px;
    height: 1200px;
    overflow: hidden;
    background:
      radial-gradient(ellipse at 40% 30%, var(--wall-light) 0%, var(--wall-mid) 55%, var(--wall-dark) 100%);
  }
  .cover-art {
    position: absolute;
    inset: 0;
    width: 1200px;
    height: 1200px;
  }
  .podcast-label {
    font-family: "Raleway", sans-serif;
    font-weight: 200;
    font-size: 92px;
    fill: var(--silver);
    stroke: var(--silver-edge);
    stroke-width: 1.2px;
  }
  .title-line {
    font-family: "Archivo Black", sans-serif;
  }
  .title-property { font-size: 176px; fill: url(#goldFill); }
  .title-auctions { font-size: 196px; fill: url(#redFill); }
  .host-name {
    font-family: "Archivo Black", sans-serif;
    font-size: 100px;
    fill: var(--name-fill);
    stroke: var(--name-edge);
    stroke-width: 1.5px;
  }
</style>
</head>
<body>
<div class="cover">
  <svg class="cover-art" viewBox="0 0 1200 1200" xmlns="http://www.w3.org/2000/svg">
    <defs>
      <linearGradient id="goldFill" x1="0" y1="0" x2="0" y2="1">
        <stop offset="0" stop-color="var(--gold-top)"/>
        <stop offset="1" stop-color="var(--gold-bottom)"/>
      </linearGradient>
      <linearGradient id="redFill" x1="0" y1="0" x2="0" y2="1">
        <stop offset="0" stop-color="var(--red-top)"/>
        <stop offset="1" stop-color="var(--red-bottom)"/>
      </linearGradient>
      <linearGradient id="photoFill" x1="0" y1="0" x2="0" y2="1">
        <stop offset="0" stop-color="var(--photo-top)"/>
        <stop offset="0.4" stop-color="var(--photo-mid)"/>
        <stop offset="0.6" stop-color="var(--photo-suit)"/>
        <stop offset="1" stop-color="var(--photo-bottom)"/>
      </linearGradient>
      <filter id="titleShadow" x="-5%" y="-10%" width="115%" height="130%">
        <feDropShadow dx="5" dy="6" stdDeviation="3" flood-color="#000" flood-opacity="0.75"/>
      </filter>
    </defs>

    <text class="podcast-label" x="600" y="134" text-anchor="middle"
          textLength="600" lengthAdjust="spacing">PODCAST</text>

    <g class="title" filter="url(#titleShadow)">
      <text class="title-line title-property" x="88" y="396"
            textLength="1040" lengthAdjust="spacingAndGlyphs">PROPERTY</text>
      <text class="title-line title-auctions" x="84" y="584"
            textLength="990" lengthAdjust="spacingAndGlyphs">AUCTIONS</text>
    </g>

    <path class="host-photo" role="img" aria-label="Portrait photo of host Gareth Pemberley in a pinstripe suit and white shirt"
          d="M812 1200 L830 1010 Q860 930 930 905 L960 890 L920 760 Q920 668 1010 668 Q1090 668 1090 760 L1060 890 L1100 905 Q1170 930 1200 960 L1200 1200 Z"
          fill="url(#photoFill)"/>

    <text class="host-name" x="160" y="1074"
          textLength="928" lengthAdjust="spacingAndGlyphs">GARETH PEMBERLEY</text>
  </svg>
</div>
</body>
</html>
```